House Builder and Property Development Card Design and Logo

I need a business card design for a building and property development company.
Colour scheme of Dark Grey and Green, I would like it bold, sharp and professional.
No logo yet done, I'm open to options but please stay away from the usual- house, roof, hammers etc.
Thanks Lou
Updates

Please be aware that on the business card information section the VKRT # 5382917 is a licence number and my phone number 0461739258. The numbers are close together and could be mistaken as one whole number 

Thank you

                                   

Industry/Entity Type

Building

Contact Information for Business Card

HARLOW BUILD & DEVELOPMENT.
Residential Building & Property Development
Louis Harlow - Director
VKRT # 5382917
0461739258
lou@harlowbuild.com.au

Requirements
Must have
• Bold Business name
Dark grey and green colours
Should not have
• roof outline or hammer logo

```html
<!DOCTYPE html>
<html lang="en">
<head>
<meta charset="utf-8">
<title>Harlow Build &amp; Development – Business Card</title>
<link href="https://fonts.googleapis.com/css2?family=Jost:wght@500;700&family=Open+Sans:wght@400;600&display=swap" rel="stylesheet">
<style>
  :root {
    --backdrop: #e3e4e2;
    --card: #ffffff;
    --grey-dark: #6d6e71;
    --grey-mid: #6b6c6f;
    --grey-light: #b9babb;
    --green: #0db14b;
    --green-soft: #8dd49a;
    --shadow: rgba(0,0,0,0.28);
  }
  * { margin: 0; padding: 0; box-sizing: border-box; }
  html, body { width: 1200px; height: 1000px; overflow: hidden; }
  body { background: var(--backdrop); position: relative; font-family: "Open Sans", sans-serif; }

  .card {
    position: absolute;
    background: var(--card);
    box-shadow: 6px 8px 12px var(--shadow);
    overflow: hidden;
  }
  .card--front { left: 68px; top: 67px; width: 680px; height: 389px; }
  .card--back  { left: 428px; top: 537px; width: 682px; height: 384px; }

  .card__band { position: absolute; left: 0; width: 100%; }
  .card--front .card__band { top: 345px; height: 35px; }
  .card--back  .card__band { top: 342px; height: 34px; }

  /* contact block */
  .contact-name {
    position: absolute; left: 37px; top: 22px;
    font-family: "Open Sans", sans-serif; font-weight: 600;
    font-size: 19px; color: var(--grey-dark); letter-spacing: 0.2px;
  }
  .contact-rule {
    position: absolute; left: 29px; top: 50px; width: 298px; height: 4px;
    background: var(--green);
  }
  .contact-line {
    position: absolute; font-size: 16px; color: var(--grey-dark);
  }
  .contact-line--email { left: 93px; top: 62px; }
  .contact-line--phone { left: 95px; top: 99px; }
  .icon { position: absolute; }
  .icon--mail  { left: 39px; top: 64px; }
  .icon--phone { left: 50px; top: 92px; }

  /* brand block */
  .brand {
    position: absolute; text-align: center;
    font-family: "Jost", sans-serif; color: var(--grey-mid);
  }
  .brand__mark { display: block; margin: 0 auto; background: var(--green); }
  .brand__name {
    font-weight: 700; line-height: 1.12; letter-spacing: 0.5px; color: var(--grey-mid);
  }
  .brand__tagline {
    font-family: "Open Sans", sans-serif; font-weight: 600; color: var(--green);
  }
  .brand__licence {
    font-family: "Open Sans", sans-serif; font-size: 15px; color: var(--grey-dark); margin-top: 8px;
  }

  .card--front .brand { left: 160px; width: 520px; top: 78px; }
  .card--front .brand__mark { width: 58px; height: 58px; margin-bottom: 16px; }
  .card--front .brand__name { font-size: 30px; }
  .card--front .brand__tagline { font-size: 18px; margin-top: 2px; }

  .card--back .brand { left: 0; width: 682px; top: 36px; }
  .card--back .brand__mark { width: 86px; height: 86px; margin-bottom: 30px; }
  .card--back .brand__name { font-size: 42px; }
  .card--back .brand__tagline { font-size: 25px; margin-top: 4px; }
</style>
</head>
<body>

  <section class="card card--front" aria-label="Business card front">
    <p class="contact-name">Louis Harlow - Director</p>
    <div class="contact-rule"></div>

    <svg class="icon icon--mail" width="38" height="21" viewBox="0 0 38 21" aria-hidden="true">
      <rect width="38" height="21" fill="var(--green-soft)"/>
      <polyline points="0,0 19,12 38,0" fill="none" stroke="var(--grey-dark)" stroke-width="1.5"/>
    </svg>
    <p class="contact-line contact-line--email">lou@harlowbuild.com.au</p>

    <svg class="icon icon--phone" width="16" height="32" viewBox="0 0 16 32" aria-hidden="true">
      <rect x="10" y="0" width="2" height="6" fill="var(--grey-dark)"/>
      <rect x="1" y="6" width="14" height="25" rx="2" fill="var(--green-soft)"/>
      <rect x="3" y="9" width="10" height="7" fill="var(--grey-dark)"/>
      <g fill="var(--grey-dark)">
        <rect x="3" y="19" width="2" height="2"/><rect x="7" y="19" width="2" height="2"/><rect x="11" y="19" width="2" height="2"/>
        <rect x="3" y="23" width="2" height="2"/><rect x="7" y="23" width="2" height="2"/><rect x="11" y="23" width="2" height="2"/>
        <rect x="3" y="27" width="2" height="2"/><rect x="7" y="27" width="2" height="2"/><rect x="11" y="27" width="2" height="2"/>
      </g>
    </svg>
    <p class="contact-line contact-line--phone">04 61 73 92 58</p>

    <div class="brand">
      <span class="brand__mark"></span>
      <p class="brand__name">HARLOW<br>BUILD &amp; DEVELOPMENT</p>
      <p class="brand__tagline">Residential Building &amp; Property Development</p>
      <p class="brand__licence">License No. : VKRT # 5382917</p>
    </div>

    <svg class="card__band" viewBox="0 0 680 35" preserveAspectRatio="none" aria-hidden="true">
      <rect width="680" height="35" fill="var(--grey-mid)"/>
      <polygon points="302,35 365,0 680,0 680,35" fill="var(--green)"/>
    </svg>
  </section>

  <section class="card card--back" aria-label="Business card back">
    <div class="brand">
      <span class="brand__mark"></span>
      <p class="brand__name">HARLOW<br>BUILD &amp; DEVELOPMENT</p>
      <p class="brand__tagline">Residential Building &amp; Property Development</p>
    </div>

    <svg class="card__band" viewBox="0 0 682 34" preserveAspectRatio="none" aria-hidden="true">
      <rect width="682" height="34" fill="var(--grey-mid)"/>
      <polygon points="302,34 367,0 682,0 682,34" fill="var(--green)"/>
    </svg>
  </section>

</body>
</html>
```